Keystone Institute Logo & Business card

Keystone Institute - Professional ICT Training
business is a training center.
Logo and business card that have an ID.
bold publicity, distinct, and prestige image
"Building Careers That Last"
that will attract target customer to come and take a look. that will look prestige on certificate after graduation, that will serve as a business tool to attract Business and enterprise customer (let them send their staff for training)

Target Market(s)

young professionals, university students, youth building career in IT fields

Industry/Entity Type

Education

Contact Information for Business Card

Font styles to use
Sans Serif

Colors

Designer to choose colors to be used in the design.

Requirements
Must have
• Logo Identity
• uniqueness
Nice to have
• catch phrase or illustration
Should not have
• just use alphabet as logo.

```html
<!DOCTYPE html>
<html lang="en">
<head>
<meta charset="utf-8">
<title>Keystone Institute – Business Card</title>
<link rel="stylesheet" href="https://fonts.googleapis.com/css2?family=Raleway:wght@400;500&family=Lato:wght@400&display=swap">
<style>
  :root {
    --backdrop: #9e9e9e;
    --navy: #1f275a;
    --orange: #f7931e;
    --white: #ffffff;
    --ink: #222222;
  }
  * { margin: 0; padding: 0; box-sizing: border-box; }
  html, body { width: 1200px; height: 900px; overflow: hidden; }
  body {
    position: relative;
    background: var(--backdrop);
    font-family: "Lato", Arial, sans-serif;
  }
  .card {
    position: absolute;
    top: 200px;
    width: 310px;
    height: 502px;
  }
  .card--front {
    left: 253px;
    background: var(--white);
    border-radius: 62px 0 62px 0;
  }
  .card--back {
    left: 627px;
    background: var(--navy);
    border-radius: 0 62px 0 62px;
  }
  .brand-dot {
    position: absolute;
    width: 78px;
    height: 78px;
    border-radius: 50%;
    background: var(--orange);
  }
  .card--front .brand-dot { left: 106px; top: 88px; }
  .card--back .brand-dot { left: 102px; top: 160px; }
  .brand-name {
    position: absolute;
    left: 0;
    width: 100%;
    text-align: center;
    font-family: "Raleway", Arial, sans-serif;
    font-weight: 400;
    white-space: nowrap;
  }
  .card--front .brand-name { top: 191px; font-size: 25px; color: var(--navy); }
  .card--back .brand-name { top: 288px; font-size: 28px; color: var(--white); }
  .tagline {
    position: absolute;
    top: 337px;
    left: 0;
    width: 100%;
    text-align: center;
    font-family: "Raleway", Arial, sans-serif;
    font-size: 13.5px;
    color: var(--white);
    text-transform: uppercase;
    letter-spacing: 0.3px;
    white-space: nowrap;
  }
  .holder { position: absolute; left: 33px; top: 312px; }
  .holder__name {
    font-family: "Raleway", Arial, sans-serif;
    font-weight: 500;
    font-size: 21px;
    line-height: 1;
    color: var(--navy);
  }
  .holder__surname { color: var(--orange); }
  .holder__role { font-size: 13.5px; color: var(--ink); margin-top: 1px; }
  .contacts { position: absolute; left: 31px; top: 358px; list-style: none; }
  .contacts li {
    display: flex;
    align-items: center;
    gap: 5px;
    font-size: 14px;
    line-height: 18.5px;
    color: var(--ink);
  }
  .contacts svg { width: 12px; height: 12px; fill: var(--navy); flex: none; }
  .address {
    position: absolute;
    left: 34px;
    top: 422px;
    font-size: 14px;
    line-height: 18.5px;
    color: var(--ink);
    font-style: normal;
  }
</style>
</head>
<body>
  <section class="card card--front">
    <div class="brand-dot"></div>
    <div class="brand-name">Keystone Institute</div>

    <div class="holder">
      <div class="holder__name">Daniel <span class="holder__surname">Carter</span></div>
      <div class="holder__role">Managing Director</div>
    </div>

    <ul class="contacts">
      <li>
        <svg viewBox="0 0 12 12" aria-hidden="true"><path d="M1 3.5C1 2 2.5 1 6 1s5 1 5 2.5V5H8.5V3.8h-5V5H1zM2.5 6h7l1 4.5h-9z"/></svg>
        555 210 4417
      </li>
      <li>
        <svg viewBox="0 0 12 12" aria-hidden="true"><path d="M0.5 2.5h11v7h-11zM1.5 3.3v0.5L6 6.8l4.5-3V3.3L6 6.1z" fill-rule="evenodd"/></svg>
        info@keystoneinstitute.com
      </li>
      <li>
        <svg viewBox="0 0 12 12" aria-hidden="true"><rect x="2" y="1" width="8" height="10"/></svg>
        social/keystoneinstitute
      </li>
    </ul>

    <address class="address">421, Address line here,<br>45452,Country Name</address>
  </section>

  <section class="card card--back">
    <div class="brand-dot"></div>
    <div class="brand-name">Keystone Institute</div>
    <div class="tagline">Building Careers That Last</div>
  </section>
</body>
</html>
```